Brisbane IT support business needs our first business card

Hello we are a Brisbane based Information Technology company providing support and services to small and medium sized businesses. We provide a range of services and solutions.

The business name is Wattleridge Computer Services Group, or WCSG for short.

I am looking for a business card that looks professional (don't we all want that), but most importantly, it most utilize the colours in the logo attached.

Other business owners seeking our IT services, and also home users.

Business

• Please only use the blue/orange colours in logo attached

```html
<!DOCTYPE html>
<html lang="en">
<head>
<meta charset="utf-8">
<title>WCSG Business Card</title>
<link rel="stylesheet" href="https://fonts.googleapis.com/css2?family=Exo+2:wght@500;600;700&display=swap">
<style>
  :root {
    --teal: #0f5a73;
    --teal-dark: #0a4a61;
    --teal-light: #17708c;
    --orange: #f08a24;
    --white: #ffffff;
    --page: #e7e9ea;
    --card-shadow: rgba(10, 40, 55, 0.18);
  }
  * { box-sizing: border-box; margin: 0; padding: 0; }
  html, body {
    width: 1200px; height: 914px; overflow: hidden;
    background: var(--page);
    font-family: "Exo 2", sans-serif;
  }
  .sheet {
    width: 1200px; height: 914px;
    display: flex; flex-direction: column;
    align-items: center; justify-content: center; gap: 56px;
  }
  .card {
    position: relative;
    width: 620px; height: 354px;
    background: var(--white);
    box-shadow: 0 10px 28px var(--card-shadow);
    overflow: hidden;
  }
  .brand {
    position: absolute;
    display: flex; align-items: center; gap: 22px;
  }
  .brand-dot {
    width: 96px; height: 96px; border-radius: 50%;
    background: var(--teal);
  }
  .brand-name {
    font-weight: 700; font-size: 64px; letter-spacing: 2px;
    color: var(--orange); line-height: 1;
  }
  .card-back .brand { left: 50%; top: 50%; transform: translate(-50%, -50%); }
  .card-front .brand { left: 50%; top: 28px; transform: translateX(-50%); }
  .card-front .brand-dot { width: 86px; height: 86px; }
  .card-front .brand-name { font-size: 56px; }

  .info-band {
    position: absolute; left: 0; right: 0; top: 142px; height: 184px;
    background: linear-gradient(120deg, var(--teal-dark), var(--teal-light) 55%, var(--teal-dark));
  }
  .accent-stripe {
    position: absolute; left: 0; right: 0; top: 326px; height: 14px;
    background: var(--orange);
  }
  .person {
    position: absolute; left: 38px; top: 168px; color: var(--white);
  }
  .person-name {
    font-size: 25px; font-weight: 600; color: var(--orange); line-height: 1.1;
  }
  .person-role { font-size: 17px; font-weight: 500; margin-bottom: 10px; }
  .person-address { font-size: 15px; font-weight: 500; line-height: 1.35; }
  .divider {
    position: absolute; left: 318px; top: 176px; width: 1px; height: 116px;
    background: rgba(255,255,255,0.75);
  }
  .contact {
    position: absolute; left: 346px; top: 182px;
    list-style: none; color: var(--white);
    font-size: 16px; font-weight: 500;
  }
  .contact li { display: flex; align-items: center; gap: 14px; height: 33px; }
  .contact svg { width: 18px; height: 18px; flex: none; }
</style>
</head>
<body>
<main class="sheet">
  <section class="card card-back" aria-label="Card back">
    <div class="brand">
      <span class="brand-dot"></span>
      <span class="brand-name">WCSG</span>
    </div>
  </section>

  <section class="card card-front" aria-label="Card front">
    <div class="brand">
      <span class="brand-dot"></span>
      <span class="brand-name">WCSG</span>
    </div>
    <div class="info-band"></div>
    <div class="accent-stripe"></div>

    <div class="person">
      <p class="person-name">Employee Name</p>
      <p class="person-role">Managing Director</p>
      <p class="person-address">Unit 4, 18 Quarry Lane<br>Wattleridge, QLD 4000</p>
    </div>

    <div class="divider"></div>

    <ul class="contact">
      <li>
        <svg viewBox="0 0 24 24" aria-hidden="true"><path fill="#f08a24" d="M6.6 10.8a15 15 0 0 0 6.6 6.6l2.2-2.2a1 1 0 0 1 1-.25 11.4 11.4 0 0 0 3.6.57 1 1 0 0 1 1 1V20a1 1 0 0 1-1 1A17 17 0 0 1 3 4a1 1 0 0 1 1-1h3.5a1 1 0 0 1 1 1c0 1.25.2 2.45.57 3.57a1 1 0 0 1-.25 1z"/></svg>
        <span>0400 555 012</span>
      </li>
      <li>
        <svg viewBox="0 0 24 24" aria-hidden="true"><rect x="2" y="5" width="20" height="14" rx="1.5" fill="#f08a24"/><path d="M3 6l9 7 9-7" fill="none" stroke="#0f5a73" stroke-width="1.6"/></svg>
        <span>hello@wcsg-example.com</span>
      </li>
      <li>
        <svg viewBox="0 0 24 24" aria-hidden="true"><circle cx="12" cy="12" r="10" fill="#f08a24"/><path d="M2 12h20M12 2c3 3 3 17 0 20M12 2c-3 3-3 17 0 20" fill="none" stroke="#0f5a73" stroke-width="1.3"/></svg>
        <span>www.wcsg-example.com</span>
      </li>
    </ul>
  </section>
</main>
</body>
</html>
```